Neue Website fuer Software-Firma (CMS: Joomla, Responsive Design)
Zielgruppe
Die VERTIS ist ein Software- und Beratungshaus im Lager- und Produktionslogistikbereich. Unsere Kunden sind Industriefirmen und Logistikdienstleister, die ein oder mehrere Laeger bewirtschaften und dafuer eine Software und mobile Datenerfassung einsetzen. Fast alle unserer Kunden haben KVT im Einsatz.
Aufgabenstellung
Unsere aktuelle Website wurde seit langem nicht mehr gepflegt und ist veraltet.
Wir moechten die neue Website gern mit dem CMS Joomla betreiben (ggf. waere auch Wordpress moeglich). Gern koennen Sie als Basis ein bereits existierendes (freies) Theme verwenden, wenn es entweder bereits alle Ansprueche erfuellt oder Sie es entsprechend anpassen.
Die neue Website soll in jedem Fall responsive sein, d.h. sowohl auf Desktop, Tablet und Smartphone funktionieren und das Design entsprechend anpassen.
Unsere aktuelle Seite steht unter www.vertis-lagerwerk.example
Eine Seite, die uns besonders gut gefaellt, ist www.quantelo.example (die sich auch teilweise an die gleichen Kunden richtet).
Wir moechten ein klares Design. Ein Beispiel, wie eines unserer Dashboards unserer Software aussieht, finden Sie anbei. Die Farbgestaltung darin wird jedoch noch geaendert. Sie wird eher in Richtung der Farbgestaltung der Quantelo-Website gehen, jedoch immer noch grundsaetzlich hell sein. Evtl. koennen Sie Elemente daraus aufgreifen? Es soll in jedem Fall ersichtlich sein, dass Website und Software von der gleichen Firma sind.
Es soll moeglichst viel mit Grafiken gearbeitet werden – aehnlich der Quantelo-Seite unter der Dia-Show. Diese muessen aber nicht zwingend farbig sein. Ein Mockup fuer einfarbige Grafiken unterhalb einer Diashow habe ich hier erstellt: https://hilde07.pagebau.example/meinewebsite-1 Bitte orientieren Sie sich aber nicht an dieser Seite selbst – das war nur ein Probierbeispiel.
Desweiteren soll die Seite suchmaschinenfreundlich sein.
In Ihren Leistungen enthalten sein soll:
- Erstellung der Homepage incl.
o Menu (wie bei Quantelo soll es ausklappbar sein und mind. 2 Ebenen koennen)
o Login-Button der einen externen Link aufruft
o Auswahl der Sprache (und damit Verlinkung zu jeweils der Homepage in der
ausgewaehlten Sprache
o Moeglichkeit zum Chat
o Suchfeld zum Durchsuchen aller S..

```html
<!DOCTYPE html>
<html lang="en">
<head>
<meta charset="utf-8">
<title>VERTIS – Warehouse Software Partners</title>
<link href="https://fonts.googleapis.com/css2?family=Lato:ital,wght@0,300;0,400;0,700;0,900;1,300&display=swap" rel="stylesheet">
<style>
:root{
  --blue:#0b3797;
  --red:#d3141b;
  --navy:#1b2431;
  --navy-2:#141c27;
  --pale:#eef2f5;
  --text:#3b3f46;
  --muted:#8b9098;
  --line:#e3e6ea;
  --white:#ffffff;
}
*{box-sizing:border-box;margin:0;padding:0}
html,body{width:1046px;height:1200px;overflow:hidden}
body{position:relative;background:var(--white);font-family:'Lato',sans-serif;color:var(--text)}
.abs{position:absolute}
a{color:inherit;text-decoration:none}

/* header */
.site-header{left:0;top:0;width:1046px;height:48px;background:var(--pale)}
.brand{left:211px;top:11px}
.brand-name{font-size:21px;font-weight:900;color:var(--blue);letter-spacing:.5px;line-height:1}
.brand-tag{font-size:6px;font-weight:400;color:var(--blue);margin-top:3px;letter-spacing:.2px}
.menu-toggle{left:318px;top:0;width:79px;height:48px;background:var(--navy);color:var(--white);display:flex;align-items:center;gap:10px;padding-left:13px;font-size:10.5px}
.burger{width:21px;height:13px;display:flex;flex-direction:column;justify-content:space-between}
.burger span{height:2px;background:var(--white)}
.util{top:17px;display:flex;align-items:center;gap:6px;font-size:8.5px;color:#59606a}
.util-login{left:620px}
.util-lang{left:690px}
.social{display:flex;gap:2px}
.social span{width:16px;height:16px;display:block}
.social .s1{background:#3b5a9a}.social .s2{background:#35a8e0}.social .s3{background:#d43c2e}
.social-top{left:788px;top:16px}

/* dropdown */
.dropdown{left:318px;top:48px;width:213px;height:115px;display:flex;z-index:3}
.dropdown ul{list-style:none;font-size:8.5px;color:var(--white)}
.dd-main{width:89px;background:var(--navy);padding:8px 0 0 8px}
.dd-main li{height:16.4px;display:flex;justify-content:space-between;padding-right:6px}
.dd-sub{flex:1;background:var(--navy-2);padding:12px 0 0 10px}
.dd-sub li{height:16.4px}
.is-active{color:var(--red)}

/* hero */
.hero{left:0;top:48px;width:1046px;height:341px;background:linear-gradient(90deg,#1e40a2 0%,#2a4ca6 30%,#5f7bb3 52%,#a9a8ad 70%,#c9bfb8 85%,#d9d3cf 100%)}
.hero-title{left:242px;top:164px;font-size:30px;font-weight:300;color:var(--white);line-height:32px}
.btn-red{left:245px;top:252px;width:143px;height:28px;background:var(--red);color:var(--white);font-size:13px;font-weight:300;display:flex;align-items:center;justify-content:center;letter-spacing:.3px}
.dots{left:508px;top:370px;display:flex;gap:4px}
.dots span{width:5px;height:5px;border-radius:50%;background:rgba(255,255,255,.55)}
.dots span:first-child{background:var(--white)}

/* expertise band */
.experts{left:0;top:389px;width:1046px;height:69px;background:var(--navy)}
.experts-label{left:0;top:389px;width:311px;height:69px;background:var(--red);color:var(--white);font-size:16px;font-weight:300;line-height:19px;padding:15px 0 0 215px}
.expert{top:405px;width:100px;text-align:center;color:var(--white);font-size:8.5px;letter-spacing:.3px}
.expert svg{display:block;margin:0 auto 6px}

/* service cards */
.card{top:474px;width:196px;height:196px}
.card-title{position:absolute;left:13px;bottom:8px;color:var(--white);font-size:15px;line-height:17px}

.chat{left:997px;top:586px;width:49px;height:49px;background:var(--red);display:flex;align-items:center;justify-content:center}

/* about + clients */
.h2{font-size:21px;font-weight:300;color:var(--blue)}
.about-title{left:218px;top:716px}
.about-lead{left:219px;top:749px;font-size:10px;font-style:italic;font-weight:300;color:var(--muted);line-height:13px}
.about-text{left:219px;top:792px;width:242px;font-size:8.2px;font-weight:400;line-height:10.5px;color:var(--text)}
.more{font-size:8.5px;color:var(--blue);display:flex;align-items:center;gap:5px}
.more::before{content:"";width:4px;height:4px;background:var(--red)}
.more-about{left:219px;top:864px}
.clients-title{left:477px;top:716px}
.clients-grid{left:478px;top:752px;width:356px;height:111px;display:grid;grid-template-columns:repeat(3,1fr);grid-template-rows:repeat(2,1fr);border:1px solid var(--line)}
.client{border-right:1px solid var(--line);border-bottom:1px solid var(--line);display:flex;align-items:center;justify-content:center;gap:5px;font-size:11px;font-weight:700;color:#b6b9be}
.client:nth-child(3n){border-right:0}
.client:nth-child(n+4){border-bottom:0}
.client .mark{width:6px;height:6px;background:#c4c7cc}
.client.featured{background:var(--white);box-shadow:0 1px 6px rgba(0,0,0,.14);color:var(--navy);position:relative}
.client.featured .mark{background:#a01c3a}
.more-clients{left:490px;top:864px}

/* cta band */
.cta{left:0;top:926px;width:1046px;height:84px;background:var(--blue)}
.cta-text{left:221px;top:957px;color:var(--white);font-size:20px;font-weight:300}
.btn-outline{left:672px;top:957px;width:160px;height:28px;border:1px solid var(--white);color:var(--white);font-size:11px;font-weight:300;display:flex;align-items:center;justify-content:center}

/* footer */
.f-col{top:1039px;font-size:8.3px;font-weight:300;line-height:13.1px;color:var(--text)}
.f-col h3{font-size:8.5px;font-weight:400;color:var(--red);margin-bottom:6px}
.f-col ul{list-style:none;padding-left:2px}
.f-col p{padding-left:2px;line-height:10.5px}
.f-col .mail{color:var(--red)}
.social-foot{left:780px;top:1041px}
.bottom-bar{left:0;top:1163px;width:1046px;height:37px;background:var(--pale)}
.legal{left:223px;top:1175px;font-size:8.3px;font-weight:300;color:var(--muted);display:flex;gap:9px}
.copy{right:218px;top:1175px;font-size:8.3px;font-weight:300;color:var(--muted)}
</style>
</head>
<body>

<header class="abs site-header"></header>
<div class="abs brand">
  <div class="brand-name">VERTIS</div>
  <div class="brand-tag">Warehouse Software Partners</div>
</div>
<div class="abs menu-toggle"><div class="burger"><span></span><span></span><span></span></div>Menu</div>
<div class="abs util util-login">
  <svg width="14" height="14" viewBox="0 0 14 14" fill="none" stroke="#59606a" stroke-width="1"><circle cx="7" cy="4.5" r="3"/><path d="M1.5 13.5c0-3.5 2.5-5 5.5-5s5.5 1.5 5.5 5z"/></svg>Login
</div>
<div class="abs util util-lang">
  <svg width="14" height="14" viewBox="0 0 14 14" fill="none" stroke="#59606a" stroke-width="1"><circle cx="7" cy="7" r="6"/><path d="M1 7h12M7 1c-2.5 3-2.5 9 0 12M7 1c2.5 3 2.5 9 0 12"/></svg>Language
</div>
<div class="abs social social-top" aria-label="Social links"><span class="s1"></span><span class="s2"></span><span class="s3"></span></div>

<nav class="abs dropdown">
  <ul class="dd-main">
    <li>About us</li>
    <li class="is-active">Services <span style="color:#fff">›</span></li>
    <li>Clients</li>
    <li>News</li>
    <li>Contact</li>
  </ul>
  <ul class="dd-sub">
    <li>KVT Development</li>
    <li>Warehouse Managemen</li>
    <li class="is-active">Automation / Integration</li>
    <li>Development</li>
    <li>Maintance</li>
  </ul>
</nav>

<section class="abs hero" role="img" aria-label="Warehouse worker using a handheld scanner between shelves, blue tinted"></section>
<h1 class="abs hero-title">We are conectiong dots in<br>your logistic business</h1>
<a class="abs btn-red">CONTACT US</a>
<div class="abs dots"><span></span><span></span><span></span><span></span></div>

<section class="abs experts"></section>
<div class="abs experts-label">We are<br>Experts in:</div>
<div class="abs expert" style="left:352px">
  <svg width="24" height="22" viewBox="0 0 24 22" fill="none" stroke="#fff" stroke-width="1"><path d="M1 7L12 1l11 6v14H1z"/><path d="M4 9h16v12H4zM8 13h8M8 15.5h8M8 18h8"/></svg>PRODUCTION
</div>
<div class="abs expert" style="left:475px">
  <svg width="24" height="22" viewBox="0 0 24 22" fill="none" stroke="#fff" stroke-width="1"><path d="M1 3h22v17H1zM9 3v6h6V3M15 14h5v4h-5z"/></svg>WAREHOUSING
</div>
<div class="abs expert" style="left:598px">
  <svg width="28" height="22" viewBox="0 0 28 22" fill="none" stroke="#fff" stroke-width="1"><path d="M7 18a5 5 0 0 1 0-10 7 7 0 0 1 13-2 5.5 5.5 0 0 1 1 12"/><path d="M14 11l4 2v4l-4 2-4-2v-4zM10 13l4 2 4-2M14 15v4"/></svg>KVT
</div>
<div class="abs expert" style="left:721px">
  <svg width="28" height="22" viewBox="0 0 28 22" fill="none" stroke="#fff" stroke-width="1"><path d="M3 17h22v4H3zM8 17V8l6-5 5 3M14 3v6M19 6l2 3M6 17v-5h4v5"/><circle cx="7" cy="19" r=".8"/><circle cx="12" cy="19" r=".8"/><circle cx="17" cy="19" r=".8"/><circle cx="22" cy="19" r=".8"/></svg>AUTOMATION
</div>

<article class="abs card" style="left:212px;background:linear-gradient(180deg,#c9b9a8 0%,#9e958f 55%,#4f5563 100%)" role="img" aria-label="Man in blue shirt scanning a box in a warehouse">
  <div class="card-title">KVT<br>Development</div>
</article>
<article class="abs card" style="left:424px;background:linear-gradient(180deg,#c99b6c 0%,#b89374 50%,#5d5750 100%)" role="img" aria-label="Team checking parcels and paperwork among cardboard boxes">
  <div class="card-title">Warehouse<br>Management</div>
</article>
<article class="abs card" style="left:637px;background:linear-gradient(180deg,#8c97a6 0%,#5d6672 50%,#2b303a 100%)" role="img" aria-label="Smiling worker beside a bottling line">
  <div class="card-title" style="left:17px">Automation<br>and Integration</div>
</article>

<div class="abs chat" aria-label="Chat">
  <svg width="22" height="18" viewBox="0 0 22 18"><path d="M2 1h18a1 1 0 0 1 1 1v10a1 1 0 0 1-1 1H9l-5 4v-4H2a1 1 0 0 1-1-1V2a1 1 0 0 1 1-1z" fill="#fff"/><circle cx="7" cy="7" r="1.2" fill="#d3141b"/><circle cx="11" cy="7" r="1.2" fill="#d3141b"/><circle cx="15" cy="7" r="1.2" fill="#d3141b"/></svg>
</div>

<h2 class="abs h2 about-title">Über uns</h2>
<p class="abs about-lead">Our top goal is clearly defined:<br>your satisfaction.</p>
<p class="abs about-text">We develop an optimal solution based on your specific internal logistics requirements. Our company will collaborate with you on the operational and technical requirements of your business and implement a software solution – either stand alone or integrated with your KVT® system.</p>
<a class="abs more more-about">Read Mroe</a>

<h2 class="abs h2 clients-title">Our clients</h2>
<div class="abs clients-grid">
  <div class="client"><span class="mark"></span>Avenor</div>
  <div class="client featured"><span class="mark"></span>Cervo</div>
  <div class="client"><span class="mark"></span>Basalt Chem</div>
  <div class="client"><span class="mark"></span>Hengard</div>
  <div class="client">Lorena</div>
  <div class="client">Sentrel</div>
</div>
<a class="abs more more-clients">Join in our family</a>

<section class="abs cta"></section>
<p class="abs cta-text">Join in our family happy clients</p>
<a class="abs btn-outline">CONTACT US</a>

<footer>
  <div class="abs f-col" style="left:218px">
    <h3>Company</h3>
    <ul><li>About us</li><li>Services</li><li>Contact us</li><li>Career</li><li>Last News</li><li>Clients</li><li>FAQ</li></ul>
  </div>
  <div class="abs f-col" style="left:323px">
    <h3>Services</h3>
    <ul><li>KVT Development</li><li>Warehouse Management</li><li>Automation / Integration</li><li>Product number 4</li><li>Product number 5</li></ul>
  </div>
  <div class="abs f-col" style="left:459px">
    <h3>United States</h3>
    <p>VERTIS -<br>Warehouse Software Partners, Inc.<br>240 Harbor Ridge Rd., Suite 310<br>Easton, MI 48190<br><span class="mail">info@vertis-lagerwerk.example</span><br>Tel: +1 555 010 4821<br>Fax: +1 555 010 4822</p>
  </div>
  <div class="abs f-col" style="left:623px">
    <h3>Germany</h3>
    <p>VERTIS GmbH -<br>Softwareloesungen der Logistik<br>Lindenweg 14<br>61999 Talheim<br><span class="mail">info@vertis-lagerwerk.example</span><br>Tel: +49 6100 50200<br>Fax: +49 6100 502029</p>
  </div>
  <div class="abs social social-foot" aria-label="Social links"><span class="s1"></span><span class="s2"></span><span class="s3"></span></div>
  <div class="abs bottom-bar"></div>
  <div class="abs legal"><span>Impring</span><span>AGB</span></div>
  <div class="abs copy">© 2017 by VERTIS GmbH / VERTIS Inc.</div>
</footer>

</body>
</html>
```